I need a business card to reflect my new qualifications.
Accredited Teacher, Accredited Valuer & Accredited Judge of Patchwork Quilting.
Fennick Lane Studio
47 Marlow Road, Kestrel Vale Vic 3745
0412 378 906 fennick@brelnet.com.au

```html
<!DOCTYPE html>
<html lang="en">
<head>
<meta charset="utf-8">
<title>Fennick Lane Studio – Business Card</title>
<link rel="stylesheet" href="https://fonts.googleapis.com/css2?family=Jost:wght@400&display=swap">
<style>
  :root {
    --page: #ffffff;
    --card: #e9e8ec;
    --maroon: #7d0f17;
    --maroon-deep: #5c0d12;
    --rose-soft: #d8a2a8;
  }
  html, body {
    margin: 0;
    padding: 0;
    width: 1200px;
    height: 364px;
    overflow: hidden;
    background: var(--page);
  }
  .stage {
    position: relative;
    width: 1200px;
    height: 364px;
    font-family: "Jost", "Futura", sans-serif;
  }
  .card {
    position: absolute;
    top: 35px;
    width: 492px;
    height: 281px;
    background: var(--card);
    overflow: hidden;
  }
  .card--front { left: 115px; }
  .card--back  { left: 622px; }

  .card__art {
    position: absolute;
    inset: 0;
    width: 492px;
    height: 281px;
  }

  .holder-name {
    position: absolute;
    left: 113px;
    top: 138px;
    margin: 0;
    font-size: 22px;
    line-height: 26px;
    font-weight: 400;
    color: var(--maroon);
    letter-spacing: 0.2px;
    white-space: nowrap;
  }
  .holder-title {
    position: absolute;
    left: 113px;
    top: 166px;
    margin: 0;
    font-size: 12px;
    line-height: 14px;
    color: var(--rose-soft);
    white-space: nowrap;
  }

  .studio-details {
    position: absolute;
    left: 32px;
    top: 178px;
    margin: 0;
    font-style: normal;
    font-size: 17.5px;
    line-height: 23.5px;
    color: var(--maroon-deep);
    white-space: nowrap;
  }
  .studio-details span { display: block; }
</style>
</head>
<body>
<div class="stage">

  <section class="card card--front">
    <svg class="card__art" viewBox="0 0 492 281">
      <defs>
        <linearGradient id="bottom-band" x1="0" y1="0" x2="1" y2="0">
          <stop offset="0" stop-color="#7d0f17"/>
          <stop offset="0.55" stop-color="#8a1e26"/>
          <stop offset="1" stop-color="#e3c9cc"/>
        </linearGradient>
        <linearGradient id="side-band" x1="0" y1="1" x2="0" y2="0">
          <stop offset="0" stop-color="#7d0f17"/>
          <stop offset="0.6" stop-color="#8a1e26"/>
          <stop offset="1" stop-color="#e3c9cc"/>
        </linearGradient>
        <linearGradient id="patch-front" x1="0" y1="1" x2="1" y2="0">
          <stop offset="0" stop-color="#7d0f17"/>
          <stop offset="0.5" stop-color="#b5404a"/>
          <stop offset="1" stop-color="#e3c9cc"/>
        </linearGradient>
      </defs>
      <polygon role="img" aria-label="Patchwork quilt squares in maroon, blue, gold and grey"
               points="0,56 30,56 45,110 70,150 120,185 175,215 215,250 225,281 0,281"
               fill="url(#patch-front)" opacity="0.9"/>
      <rect x="0" y="0" width="7" height="281" fill="url(#side-band)"/>
      <rect x="0" y="275" width="492" height="6" fill="url(#bottom-band)"/>
    </svg>
    <h1 class="holder-name">Rosalind Carver</h1>
    <p class="holder-title">accredited teacher, valuer &amp; judge of patchwork quilting</p>
  </section>

  <section class="card card--back">
    <svg class="card__art" viewBox="0 0 492 281">
      <defs>
        <linearGradient id="top-band" x1="1" y1="0" x2="0" y2="0">
          <stop offset="0" stop-color="#7d0f17"/>
          <stop offset="0.55" stop-color="#8a1e26"/>
          <stop offset="1" stop-color="#e3c9cc"/>
        </linearGradient>
        <linearGradient id="right-band" x1="0" y1="0" x2="0" y2="1">
          <stop offset="0" stop-color="#7d0f17"/>
          <stop offset="0.7" stop-color="#7d0f17"/>
          <stop offset="1" stop-color="#8a1e26"/>
        </linearGradient>
        <linearGradient id="patch-back" x1="1" y1="0" x2="0" y2="1">
          <stop offset="0" stop-color="#7d0f17"/>
          <stop offset="0.5" stop-color="#b5404a"/>
          <stop offset="1" stop-color="#e3c9cc"/>
        </linearGradient>
      </defs>
      <polygon role="img" aria-label="Patchwork quilt squares in maroon, blue, gold and grey"
               points="280,0 492,0 492,217 445,217 425,180 410,120 360,75 300,50 280,40"
               fill="url(#patch-back)" opacity="0.9"/>
      <rect x="0" y="0" width="492" height="6" fill="url(#top-band)"/>
      <rect x="485" y="0" width="7" height="281" fill="url(#right-band)"/>
    </svg>
    <address class="studio-details">
      <span class="studio-details__name">Fennick Lane Studio</span>
      <span class="studio-details__street">47 Marlow Road, Kestrel Vale Vic 3745</span>
      <span class="studio-details__contact">0412 378 906 fennick@brelnet.com.au</span>
    </address>
  </section>

</div>
</body>
</html>
```